" Empresa de desenvolvimento humano, que trabalha principalmente a gestão dentro do ambiente de trabalho através de treinamento, consultoria e coaching. O principal conceito é que cada pessoa é única e seu auto-conhecimento é a chave para seu sucesso. "

```html
<!DOCTYPE html>
<html lang="pt">
<head>
<meta charset="UTF-8">
<title>Agradecimentos</title>
<link href="https://fonts.googleapis.com/css2?family=Questrial&display=swap" rel="stylesheet">
<style>
  :root {
    --page-bg: #ffffff;
    --slide-bg: #ffffff;
    --title-blue: #2f6fb3;
    --body-text: #4d6a93;
    --accent-blue: #1f86d0;
    --accent-grey: #4a4d52;
    --photo-light: #f5f7f8;
    --photo-mid: #e6ecf0;
  }
  html, body {
    margin: 0;
    padding: 0;
    width: 1200px;
    height: 1200px;
    overflow: hidden;
    background: var(--page-bg);
  }
  .slide {
    position: absolute;
    left: 0;
    top: 240px;
    width: 1200px;
    height: 708px;
    background: var(--slide-bg);
    overflow: hidden;
  }
  .slide-art {
    position: absolute;
    inset: 0;
    width: 1200px;
    height: 708px;
  }
  .slide-title {
    position: absolute;
    left: 18px;
    top: 56px;
    margin: 0;
    font-family: "Questrial", sans-serif;
    font-weight: 400;
    font-size: 62px;
    line-height: 1;
    letter-spacing: 3px;
    color: var(--title-blue);
    -webkit-text-stroke: 1.4px var(--title-blue);
    white-space: nowrap;
  }
  .slide-body {
    position: absolute;
    left: 19px;
    top: 166px;
    font-family: "Questrial", sans-serif;
    font-size: 28px;
    line-height: 37px;
    color: var(--body-text);
    white-space: nowrap;
  }
  .slide-body p { margin: 0; }
</style>
</head>
<body>
  <section class="slide">
    <svg class="slide-art" viewBox="0 0 1200 708" xmlns="http://www.w3.org/2000/svg">
      <defs>
        <linearGradient id="photo-tones" x1="0" y1="0" x2="1" y2="1">
          <stop offset="0" stop-color="var(--photo-mid)"/>
          <stop offset="0.5" stop-color="var(--photo-light)"/>
          <stop offset="1" stop-color="var(--photo-mid)"/>
        </linearGradient>
      </defs>
      <path class="photo-area" role="img" aria-label="Fotografia de uma margarida branca vista de perto sobre céu claro"
            d="M 636 0 C 900 160, 900 540, 600 708 L 1200 708 L 1200 0 Z" fill="url(#photo-tones)"/>
      <path class="accent-band-blue" d="M 570 0 L 590 0 C 850 170, 850 540, 585 708 L 568 708 C 800 530, 800 180, 570 0 Z" fill="var(--accent-blue)"/>
      <path class="accent-band-grey" d="M 590 0 L 636 0 C 900 160, 900 540, 600 708 L 585 708 C 850 540, 850 170, 590 0 Z" fill="var(--accent-grey)"/>
    </svg>

    <h1 class="slide-title">AGRADECIMENTOS</h1>

    <div class="slide-body">
      <p>Donec a ultricies purus. Suspendisse<br>dictum nunc nec magna suscipit<br>bibendum. Maecenas turpis sapien,<br>elementum vitae tellus sit amet, efficitur<br>bibendum tortor.</p>
      <p>Sed commodo diam ut nisl sodales<br>consectetur. In hac habitasse platea<br>dictumst. Proin ut augue at augue<br>euismod malesuada.</p>
      <p>Donec a metus sed ligula ultrices<br>vulputate. Nullam convallis interdum mi,<br>in ornare ligula vestibulum vel. Donec<br>faucibus, elit eu viverra posuere, libero<br>enim.</p>
    </div>
  </section>
</body>
</html>
```